Cover graphic for law firm brochure

We need cover art designed for a brochure which will also serve for our client’s design on social media banners. We would love a creative design that could incorporate the design elements from the circle in the logo or other design elements for a Washington, D.C.-based law firm that specializes in government contracting. Attached is their logo for colors and brand feel. The front page of the brochure needs to have their logo on it. A design element using their logo or the circle from their logo, would be great to see. The planes need to be removed. We would love to see options for the back but our client likes this image.

We would love to see abstract art creation using the colors from the logo, you can also do a pop of gold from the capital building.

The dimensions are 24x8. We will upload a high-resolution logo and the full brochure in the coming day or two.

If you are going to add text to the front please use this text: Hale & Norcott is a boutique law firm built to provide exceptional representation to government contractors.

The other option is to do something grey scale with pops of colors with the DC Skyline, American Flags (with one in color), or other items. On the back of the cover, I would love to see a design option that carries through from the front. You can use elements from the capital building that is already there or other images.

Please do not reach out to the client directly as they are busy. Please only communicate through the platform.

We are excited to see your creative designs!
Updates

I will be sending out the high-res logo and brochure dimensions shortly.

Target Market(s)

areospace and defense industry

Industry/Entity Type

Legal

Font styles to use
Other font styles liked:
• See logo

Colors

Designer to choose colors to be used in the design.

Requirements
Must have
• If doing a graphic creation, use of colors from logo and abstract design that is conservative, upscale and elegant feeling. If doing a cover with an image a picture that is similar to the one below or something that is related.
Should not have
• Law related images of scales, gavels or other law items, please do not use an image of the capital on the front as that is the back image.

```html
<!DOCTYPE html>
<html lang="en">
<head>
<meta charset="utf-8">
<title>Hale &amp; Norcott — Brochure Cover</title>
<link rel="stylesheet" href="https://fonts.googleapis.com/css2?family=Cinzel:wght@400;700&family=Poppins:wght@500&display=swap">
<style>
  :root {
    --page: #ffffff;
    --navy: #17284a;
    --navy-deep: #0f1c36;
    --gold: #f5b21c;
    --white: #ffffff;
    --steel: #6f7279;
    --flag-grey: #7a7b80;
    --flag-red: #8a4a55;
    --sky: #3d78c9;
    --stone: #e6dcc4;
  }
  * { margin: 0; padding: 0; box-sizing: border-box; }
  html, body { width: 1067px; height: 1200px; overflow: hidden; background: var(--page); }
  .cover {
    position: absolute; left: 0; top: 66px;
    width: 1067px; height: 1067px; overflow: hidden;
    background: var(--navy);
  }
  .cover-art { position: absolute; inset: 0; }
  .brand {
    position: absolute; left: 0; right: 0; top: 668px;
    display: flex; justify-content: center; align-items: center; gap: 18px;
  }
  .brand-ring {
    width: 80px; height: 80px; border-radius: 50%;
    border: 3px solid var(--white);
  }
  .brand-name {
    font-family: "Cinzel", serif; font-weight: 400; font-size: 30px;
    color: var(--white); letter-spacing: 2px;
  }
  .headline { position: absolute; left: 0; right: 0; top: 785px; text-align: center; }
  .headline-lead {
    font-family: "Poppins", sans-serif; font-weight: 500; font-size: 30px;
    color: var(--white); letter-spacing: 17px; line-height: 40px;
    padding-left: 17px;
  }
  .headline-main {
    font-family: "Cinzel", serif; font-weight: 700; font-size: 46px;
    color: var(--gold); line-height: 56px; margin-top: 6px;
  }
  .headline-join {
    display: flex; justify-content: center; align-items: center; gap: 14px;
    font-family: "Cinzel", serif; font-size: 34px; color: var(--white); line-height: 40px;
  }
  .headline-join::before, .headline-join::after {
    content: ""; width: 150px; height: 2px; background: var(--white);
  }
  .headline-sub {
    font-family: "Cinzel", serif; font-weight: 400; font-size: 44px;
    color: var(--white); line-height: 52px;
  }
</style>
</head>
<body>
  <main class="cover">
    <svg class="cover-art" width="1067" height="1067" viewBox="0 0 1067 1067">
      <defs>
        <linearGradient id="flagTone" x1="0" y1="0" x2="1" y2="1">
          <stop offset="0" stop-color="var(--flag-red)"/>
          <stop offset="0.35" stop-color="var(--flag-grey)"/>
          <stop offset="0.7" stop-color="var(--flag-red)"/>
          <stop offset="1" stop-color="var(--flag-grey)"/>
        </linearGradient>
        <linearGradient id="cityTone" x1="0" y1="0" x2="0" y2="1">
          <stop offset="0" stop-color="#1b2d52"/>
          <stop offset="1" stop-color="var(--navy-deep)"/>
        </linearGradient>
        <linearGradient id="capitolTone" x1="0" y1="0" x2="0" y2="1">
          <stop offset="0" stop-color="var(--sky)"/>
          <stop offset="0.45" stop-color="#a9b8cf"/>
          <stop offset="0.7" stop-color="var(--stone)"/>
          <stop offset="1" stop-color="#b9a783"/>
        </linearGradient>
      </defs>
      <rect class="flag-backdrop" x="0" y="0" width="1067" height="700" fill="url(#flagTone)" role="img" aria-label="Waving American flag in muted grey and red tones"/>
      <path class="arc-steel" d="M0,650 Q533,280 1067,640 L1067,1067 L0,1067 Z" fill="var(--steel)"/>
      <path class="arc-white" d="M0,637 Q533,266 1067,627 L1067,1067 L0,1067 Z" fill="var(--white)"/>
      <path class="arc-gold" d="M0,626 Q533,252 1067,614 L1067,622 Q533,262 0,632 Z" fill="var(--gold)"/>
      <path class="city-band" d="M0,660 Q533,292 1067,650 L1067,1067 L0,1067 Z" fill="url(#cityTone)" role="img" aria-label="Dusk city skyline in dark navy"/>
      <circle class="ring-outer" cx="527" cy="330" r="297" fill="var(--white)"/>
      <path class="ring-swoosh" d="M300,520 A250,250 0 0 0 740,540 A262,262 0 0 1 300,520 Z" fill="var(--navy)"/>
      <circle class="capitol-photo" cx="533" cy="328" r="251" fill="url(#capitolTone)" role="img" aria-label="Photograph of the domed capitol building against blue sky"/>
    </svg>

    <div class="brand">
      <div class="brand-ring"></div>
      <div class="brand-name">HALE &amp; NORCOTT</div>
    </div>

    <div class="headline">
      <p class="headline-lead">SOLUTIONS FOR</p>
      <p class="headline-main">GOVERNMENT CONTRACTORS</p>
      <p class="headline-join">&amp;</p>
      <p class="headline-sub">TECHNOLOGY INNOVATORS</p>
    </div>
  </main>
</body>
</html>
```